Electronic Letterhead for The Harborline Partners, LLC

I would like to have an electronic letterhead layout using Word for first and second page letterhead using my previously designed logo. The logo was successfully designed by a designer for the Pixel Bazaar. I would like to only use the "C" portion of the logo on the second page. I would like the designer that designed my logo to be included in the designers that participate in this competition.

Target Market(s)

My clients are typically governmental entities or financial entities

Industry/Entity Type

Electronic

Font styles to use
Sans Serif

Requirements
Must have
• Utilize existing logo
Nice to have
• Fist and second page letterhead design in electronic format (Word)

```html
<!DOCTYPE html>
<html lang="en">
<head>
<meta charset="utf-8">
<title>The Harborline Partners, LLC — Letterhead</title>
<link href="https://fonts.googleapis.com/css2?family=Questrial&family=Tinos&display=swap" rel="stylesheet">
<style>
  :root{
    --backdrop:#e9e4dc;
    --paper:#ffffff;
    --brand-blue:#1f4f94;
    --ink:#1c1c1c;
    --ring:#cfdbe8;
    --ring-bar:#e2e2e2;
    --shadow:rgba(40,30,20,.35);
  }
  *{margin:0;padding:0;box-sizing:border-box}
  html,body{width:1200px;height:1000px;overflow:hidden;background:var(--backdrop)}
  body{position:relative;font-family:"Questrial",sans-serif;color:var(--ink)}

  .sheet{position:absolute;top:172px;width:462px;height:656px;background:var(--paper);
    box-shadow:4px 6px 10px var(--shadow);overflow:hidden}
  .sheet--first{left:108px}
  .sheet--second{left:630px}

  .backdrop-mark{position:absolute;border-radius:50%;background:var(--ring);opacity:.85}
  .sheet--first .backdrop-mark{left:245px;top:415px;width:230px;height:230px}
  .sheet--second .backdrop-mark{left:205px;top:405px;width:262px;height:262px}

  .label{font-family:"Tinos",serif;color:var(--brand-blue);font-size:8.5px;letter-spacing:.2px;text-transform:uppercase}
  .small{font-size:7px;line-height:8.4px}

  .brand{position:absolute;left:38px;top:37px;display:flex;align-items:center;gap:7px}
  .brand__dot{width:30px;height:30px;border-radius:50%;background:var(--brand-blue)}
  .brand__name{font-family:"Tinos",serif;color:var(--brand-blue);font-size:12px;line-height:12.5px}

  .contact{position:absolute;right:40px;top:35px;text-align:right}
  .contact .label{margin-top:10px}
  .contact .label:first-child{margin-top:0}

  .meta{position:absolute;left:0;top:165px;width:82px;text-align:right}
  .meta .label{margin-top:11px}
  .meta .label:first-child{margin-top:0}

  .letter-body{position:absolute;left:112px;width:310px;font-size:7px;line-height:9.3px}
  .sheet--first .letter-body{top:165px}
  .sheet--second .letter-body{top:32px;left:113px;width:316px}
  .letter-body p{margin-bottom:9px}
  .greeting{color:var(--brand-blue);margin-bottom:9px}

  .page-number{position:absolute}
  .sheet--first .page-number{left:53px;top:587px}
  .sheet--second .page-number{left:54px;top:33px}

  .signature{width:58px;height:30px;margin:8px 0 4px;background:linear-gradient(90deg,#d5e1f2,#e9eef7);border-radius:3px}
  .signer{color:var(--brand-blue)}

  .footer-contact{position:absolute;left:55px;top:501px}
  .footer-contact .label{margin-top:10px}
  .footer-contact .label:first-child{margin-top:0}
</style>
</head>
<body>

<section class="sheet sheet--first">
  <div class="backdrop-mark" aria-hidden="true"></div>

  <div class="brand">
    <span class="brand__dot" aria-hidden="true"></span>
    <span class="brand__name">The Harborline<br>Partners, LLC</span>
  </div>

  <div class="contact">
    <div class="label">Address</div>
    <div class="small">Number, Address Line<br>City, Country, Postcode</div>
    <div class="label">Numbers</div>
    <div class="small">P: 888 888 8888<br>F: 999 999 9999</div>
    <div class="label">Online</div>
    <div class="small">E: name@harborlinemail.com<br>W: www.harborlinepartners.com</div>
  </div>

  <div class="meta">
    <div class="label">Subject</div>
    <div class="small">Lorem Ipsum</div>
    <div class="label">Date</div>
    <div class="small">07/08/2020</div>
    <div class="label">Receiver</div>
    <div class="small">John Doe</div>
  </div>

  <div class="letter-body">
    <div class="greeting">Dear Client</div>
    <p>Lorem ipsum dolor sit amet, consectetur adipisicing elit. Sed do eiusmod tempor incididunt ut labore et dolore magna aliqua. Ut enim ad minim veniam, quis nostrud exercitation ullamco laboris nisi ut aliquip ex ea commodo consequat. Duis aute irure dolor in reprehenderit in voluptate velit esse cillum dolore eu fugiat nulla pariatur. Excepteur sint occaecat cupidatat non proident, sunt in culpa qui officia deserunt mollit anim id est laborum.</p>
    <p>Sed ut perspiciatis unde omnis iste natus error sit voluptatem accusantium doloremque laudantium, totam rem aperiam, eaque ipsa quae ab illo inventore veritatis et quasi architecto beatae vitae dicta sunt explicabo.</p>
    <p>Nemo enim ipsam voluptatem quia voluptas sit aspernatur aut odit aut fugit, sed quia consequuntur magni dolores eos qui ratione voluptatem sequi nesciunt. Neque porro quisquam est, qui dolorem ipsum quia dolor sit amet, consectetur, adipisci velit, sed quia non numquam eius modi tempora incidunt ut labore et dolore magnam aliquam quaerat voluptatem. Duis aute irure dolor in quia est reprehenderit in voluptate velit esse cillum dolore eu fugiat nulla pariatur.</p>
    <p>Excepteur sint occaecat cupidatat non proident, sunt in culpa qui officia deserunt mollit anim id est dolor in reprehenderit. Excepteur sint occaecat cupidatat non proident, sunt in culpa qui officia deserunt mollit anim id est laborum. In voluptate velit esse cillum dolore eu fugiat nulla pariatur laborum.</p>
    <p>Lorem ipsum dolor sit amet, consectetur adipisicing elit. Sed do eiusmod tempor incididunt ut labore et dolore magna aliqua. Ut enim ad minim veniam, quis nostrud exercitation ullamco laboris nisi ut aliquip ex ea commodo consequat. Duis aute irure dolor in reprehenderit in voluptate velit esse cillum dolore eu fugiat nulla pariatur. Excepteur sint occaecat cupidatat non proident, sunt in culpa qui officia deserunt mollit anim id est laborum.</p>
    <p>Nemo enim ipsam voluptatem quia voluptas sit aspernatur aut odit aut fugit, sed quia consequuntur magni dolores eos qui ratione voluptatem sequi nesciunt. Neque porro quisquam est, qui dolorem ipsum quia dolor sit amet, consectetur, adipisci velit, sed quia non numquam eius modi tempora incidunt ut labore et dolore magnam aliquam quaerat voluptatem. Duis aute irure dolor in quia est reprehenderit in voluptate velit esse cillum dolore eu fugiat nulla pariatur.</p>
    <p>Excepteur sint occaecat cupidatat non proident, sunt in culpa qui officia deserunt mollit anim id est dolor in reprehenderit. Excepteur sint occaecat cupidatat non proident, sunt in culpa qui officia deserunt mollit anim id est laborum. In voluptate velit esse cillum dolore eu fugiat nulla pariatur laborum.</p>
    <p>Wicepteur sint occaecat cupidatat non proident, sunt in culpa qui officia deserunt mollit anim id est dolor in reprehenderit. Excepteur sint occaecat cupidatat non proident, sunt in culpa qui officia deserunt mollit anim id est laborum. In voluptate velit esse cillum dolore eu fugiat nulla pariatur reprehenderit. Excepteur sint occaecat.</p>
  </div>

  <div class="label page-number">Page 1</div>
</section>

<section class="sheet sheet--second">
  <div class="backdrop-mark" aria-hidden="true"></div>

  <div class="label page-number">Page 2</div>

  <div class="letter-body">
    <p>Lorem ipsum dolor sit amet, consectetur adipisicing elit. Sed do eiusmod tempor incididunt ut labore et dolore magna aliqua. Ut enim ad minim veniam, quis nostrud exercitation ullamco laboris nisi ut aliquip ex ea commodo consequat. Duis aute irure dolor in reprehenderit in voluptate velit esse cillum dolore eu fugiat nulla pariatur. Excepteur sint occaecat cupidatat non proident, sunt in culpa qui officia deserunt mollit anim id est laborum.</p>
    <p>Sed ut perspiciatis unde omnis iste natus error sit voluptatem accusantium doloremque laudantium, totam rem aperiam, eaque ipsa quae ab illo inventore veritatis et quasi architecto beatae vitae dicta sunt explicabo.</p>
    <p>Nemo enim ipsam voluptatem quia voluptas sit aspernatur aut odit aut fugit, sed quia consequuntur magni dolores eos qui ratione voluptatem sequi nesciunt. Neque porro quisquam est, qui dolorem ipsum quia dolor sit amet, consectetur, adipisci velit, sed quia non numquam eius modi tempora incidunt ut labore et dolore magnam aliquam quaerat voluptatem. Duis aute irure dolor in quia est reprehenderit in voluptate velit esse cillum dolore eu fugiat nulla pariatur.</p>
    <p>Excepteur sint occaecat cupidatat non proident, sunt in culpa qui officia deserunt mollit anim id est dolor in reprehenderit. Excepteur sint occaecat cupidatat non proident, sunt in culpa qui officia deserunt mollit anim id est laborum. In voluptate velit esse cillum dolore eu fugiat nulla pariatur laborum.</p>
    <p>Lorem ipsum dolor sit amet, consectetur adipisicing elit. Sed do eiusmod tempor incididunt ut labore et dolore magna aliqua. Ut enim ad minim veniam, quis nostrud exercitation ullamco laboris nisi ut aliquip ex ea commodo consequat. Duis aute irure dolor in reprehenderit in voluptate velit esse cillum dolore eu fugiat nulla pariatur. Excepteur sint occaecat cupidatat non proident, sunt in culpa qui officia deserunt mollit anim id est laborum.</p>
    <div>Yours Sincerely</div>
    <div class="signature" role="img" aria-label="Handwritten signature of the sender"></div>
    <div class="signer">Jane Doe</div>
    <div>Managing Director</div>
  </div>

  <div class="footer-contact">
    <div class="label">Address</div>
    <div class="small">Number, Address Line<br>City, Country, Postcode</div>
    <div class="label">Numbers</div>
    <div class="small">P: 888 888 8888<br>F: 999 999 9999</div>
    <div class="label">Online</div>
    <div class="small">E: name@harborlinemail.com<br>W: www.harborlinepartners.com</div>
  </div>
</section>

</body>
</html>
```